Wanderfolk Postcard Flyer

I run a group called 'The London Wanderfolk Group', we explore London's history and culture through it's museums, art galleries, historical buildings, guided walks, theatre etc

I would need a design for a postcard sized flyer, full colour, double sided which will attract people to join the group if handed one.

Target Market(s)

People who like exploring museums, galleries, culture etc.

Industry/Entity Type

Group

Requirements
Must have
• The below needs to be included on the front:

www.wanderfolk-example.org
The London Wanderfolk Group
Meet like minded people!
Explore London's history and culture!
Join online

Also the panorama in the file attached.

The below needs to be included on the back:

www.wanderfolk-example.org
We organise trips visiting: museums, art galleries, historical buildings, stately homes, theatre, guided walks, social/quiz nights, day trips out of London.

Also include some pictures of in the Word doc attached.

```html
<!DOCTYPE html>
<html lang="en">
<head>
<meta charset="utf-8">
<title>The London Wanderfolk Group – Postcard Flyer</title>
<link href="https://fonts.googleapis.com/css2?family=Arvo:wght@700&family=Open+Sans:wght@400&display=swap" rel="stylesheet">
<style>
  :root {
    --page: #e9e6e1;
    --card-red: #a3142b;
    --card-red-dark: #8a0f22;
    --band-blue: #4d72b8;
    --bullet-blue: #7fa6e0;
    --white: #ffffff;
    --gold: #e0b33a;
    --sepia-light: #e8dcc3;
    --sepia-dark: #9c8563;
  }
  * { box-sizing: border-box; margin: 0; padding: 0; }
  html, body { width: 1200px; height: 775px; overflow: hidden; }
  body { background: var(--page); position: relative; font-family: "Arvo", Georgia, serif; }

  .card {
    position: absolute; top: 45px; width: 480px; height: 685px;
    background: linear-gradient(180deg, var(--card-red) 0%, var(--card-red-dark) 100%);
    box-shadow: 0 6px 18px rgba(0,0,0,.25); overflow: hidden; color: var(--white);
  }
  .card--back { left: 90px; }
  .card--front { left: 630px; }

  .url-band {
    position: absolute; left: 0; right: 0; bottom: 0; height: 58px;
    background: var(--band-blue); display: flex; align-items: center; justify-content: center;
    font-family: "Open Sans", Arial, sans-serif; font-size: 21px; letter-spacing: 5px;
  }

  .photo {
    position: absolute; border: 6px solid var(--white);
    background-clip: padding-box;
  }

  /* Back side */
  .back-title { position: absolute; left: 30px; top: 30px; font-size: 30px; line-height: 1.1; }
  .activity-list { list-style: none; font-size: 21px; line-height: 1.2; }
  .activity-list--top { position: absolute; left: 30px; top: 130px; }
  .activity-list--top li::before {
    content: ""; display: inline-block; width: 7px; height: 7px; background: var(--bullet-blue);
    margin-right: 10px; vertical-align: middle;
  }
  .activity-list--bottom { position: absolute; right: 185px; top: 420px; text-align: right; }
  .activity-list--bottom li::after {
    content: ""; display: inline-block; width: 7px; height: 7px; background: var(--bullet-blue);
    margin-left: 10px; vertical-align: middle;
  }
  .photo-strip { position: absolute; left: 0; top: 265px; width: 300px; height: 110px; background: var(--white); }
  .photo-column { position: absolute; left: 290px; top: 110px; width: 170px; height: 495px; background: var(--white); }
  .photo--castle { left: 8px; top: 270px; width: 130px; height: 100px; background: linear-gradient(180deg,#b9c7d6,#8a8466 60%,#6f7a4c); border: none; }
  .photo--social { left: 145px; top: 270px; width: 145px; height: 100px; background: linear-gradient(135deg,#5a4638,#a88466 50%,#3b2f2a); border: none; }
  .photo--ceiling { left: 298px; top: 118px; width: 154px; height: 155px; background: linear-gradient(180deg,#b58a4e,#6b4a2c 60%,#d8cbb2); border: none; }
  .photo--statue { left: 298px; top: 281px; width: 154px; height: 170px; background: linear-gradient(180deg,#c9c7bf,#8b8576 55%,#d9d6cc); border: none; }
  .photo--house { left: 298px; top: 459px; width: 154px; height: 138px; background: linear-gradient(180deg,#e9e5dc,#3a3230 55%,#7b6f62); border: none; }

  /* Front side */
  .front-title { position: absolute; right: 24px; top: 30px; text-align: right; font-size: 33px; line-height: 1.1; }
  .title-rule { position: absolute; left: 120px; right: 24px; top: 142px; height: 3px; }
  .panorama { position: absolute; left: 0; right: 0; top: 150px; height: 185px;
    background: linear-gradient(180deg, var(--sepia-light) 0%, var(--sepia-dark) 70%, var(--sepia-light) 100%); }
  .photo--cathedral { left: -6px; top: 300px; width: 135px; height: 165px; background: linear-gradient(180deg,#d7e3ef,#9f9a86 40%,#6e6a55); }
  .photo--walk { left: 122px; top: 305px; width: 170px; height: 175px; background: linear-gradient(180deg,#7da05a,#a9a392 55%,#5d5a55); }
  .photo--pond { left: 284px; top: 310px; width: 180px; height: 160px; background: linear-gradient(180deg,#b8d3ef,#5f7a45 55%,#8fb0cf); }
  .front-copy { position: absolute; left: 0; right: 0; top: 510px; text-align: center; font-size: 19px; line-height: 1.3; }
  .front-copy .join { margin-top: 8px; font-size: 17px; }
</style>
</head>
<body>

<section class="card card--back" aria-label="Flyer back">
  <h2 class="back-title">We organise<br>trips visiting:</h2>
  <ul class="activity-list activity-list--top">
    <li>Museums</li>
    <li>Art galleries</li>
    <li>Historical buildings</li>
    <li>Stately homes</li>
  </ul>

  <div class="photo-strip"></div>
  <div class="photo photo--castle" role="img" aria-label="Photo of a stone castle gatehouse"></div>
  <div class="photo photo--social" role="img" aria-label="Photo of group members at a social night"></div>

  <div class="photo-column"></div>
  <div class="photo photo--ceiling" role="img" aria-label="Photo of a painted hall ceiling"></div>
  <div class="photo photo--statue" role="img" aria-label="Photo of a statue outside a historic building"></div>
  <div class="photo photo--house" role="img" aria-label="Photo of a Tudor timber-framed house"></div>

  <ul class="activity-list activity-list--bottom">
    <li>Theatre</li>
    <li>Guided walks</li>
    <li>Social/quiz nights</li>
    <li>Day trips out of London</li>
  </ul>

  <div class="url-band">www.wanderfolk-example.org</div>
</section>

<section class="card card--front" aria-label="Flyer front">
  <h1 class="front-title">The London<br>Wanderfolk Group</h1>
  <svg class="title-rule" viewBox="0 0 336 3" preserveAspectRatio="none" aria-hidden="true">
    <defs>
      <linearGradient id="ruleFade" x1="0" x2="1">
        <stop offset="0" stop-color="#e0b33a" stop-opacity="0"/>
        <stop offset="1" stop-color="#e0b33a"/>
      </linearGradient>
    </defs>
    <rect width="336" height="3" fill="url(#ruleFade)"/>
  </svg>

  <div class="panorama" role="img" aria-label="Historic engraved panorama of the London skyline along the Thames"></div>
  <div class="photo photo--cathedral" role="img" aria-label="Photo of a Gothic cathedral tower"></div>
  <div class="photo photo--walk" role="img" aria-label="Photo of a group on a guided walk"></div>
  <div class="photo photo--pond" role="img" aria-label="Photo of a park lake"></div>

  <div class="front-copy">
    <p>Explore London's history and culture!</p>
    <p>Meet like minded people!</p>
    <p class="join">Join online</p>
  </div>

  <div class="url-band">www.wanderfolk-example.org</div>
</section>

</body>
</html>
```